New Business Card Design Project - RK Ledgerwise & Filing Partners, LLC

Below is a sample image of the card (TM Bookkeeping). I would like to have a designed business card that looks very similar (Front & Back). In addition, I would like to keep the same colors as well. I attached my Business Logo (RK Ledgerwise & Filing Partners, LLC) that will be on my website.

Target Market(s)

Executives, Business Owners, Board of Directors, Chief Financial Officers

Contact Information for Business Card

Font styles to use
Serif

Colors
0c5ba6
ffffff
5c5c5c

Requirements
Must have
• My Name: Malcolm Ferris, CPA
• Position: Owner
• Phone: (240) 555-0148
• Email: Mferris@rkledgerwise.example
• Website: www.Rkledgerwise.example
• Address: 4736 Ferncliff Ave #2093
• Dunmore Falls, MD 21990
Nice to have
• Same design & color scheme as TM Bookkeepnig Business card sample attached

```html
<!DOCTYPE html>
<html lang="en">
<head>
<meta charset="utf-8">
<title>RK Ledgerwise &amp; Filing Partners — Business Card</title>
<link href="https://fonts.googleapis.com/css2?family=Tinos:wght@400;700&display=swap" rel="stylesheet">
<style>
  :root {
    --brand-blue: #0c5ba6;
    --paper: #ffffff;
    --slate: #5c5c5c;
    --ink: #3a3a3a;
    --backdrop: #e6e7ea;
  }
  * { margin: 0; padding: 0; box-sizing: border-box; }
  html, body { width: 1200px; height: 880px; overflow: hidden; }
  body {
    background: var(--backdrop);
    font-family: "Tinos", "Times New Roman", serif;
    position: relative;
  }
  .card {
    position: absolute;
    width: 620px;
    height: 354px;
    border-radius: 22px;
    overflow: hidden;
    box-shadow: 0 10px 28px rgba(0,0,0,0.22);
  }
  .card--front { left: 90px; top: 60px; background: var(--brand-blue); }
  .card--back  { left: 490px; top: 466px; background: var(--paper); }

  .brand {
    position: absolute;
    display: flex;
    align-items: center;
    gap: 14px;
    font-weight: 400;
    text-transform: uppercase;
  }
  .brand__mark { width: 18px; height: 18px; flex: none; }
  .brand__name { line-height: 1.15; }
  .brand__line1 { display: block; font-size: 30px; letter-spacing: 1.5px; }
  .brand__line2 { display: block; font-size: 15px; letter-spacing: 4px; }

  .card--front .brand { left: 50%; top: 50%; transform: translate(-50%, -50%); color: var(--paper); }
  .card--front .brand__mark { background: var(--paper); }

  .card--back .brand { left: 36px; top: 150px; color: var(--brand-blue); }
  .card--back .brand__line1 { font-size: 22px; letter-spacing: 1px; }
  .card--back .brand__line2 { font-size: 11px; letter-spacing: 2.6px; }
  .card--back .brand__mark { width: 14px; height: 14px; background: var(--slate); }

  .divider {
    position: absolute;
    left: 300px; top: 58px;
    width: 1.5px; height: 150px;
    background: var(--brand-blue);
  }
  .contact {
    position: absolute;
    left: 320px; top: 52px;
    color: var(--ink);
    font-size: 14px;
    line-height: 1.35;
  }
  .contact__name { font-size: 18px; color: var(--slate); }
  .contact__role { color: var(--brand-blue); font-size: 15px; margin-bottom: 8px; }
  .contact__row { display: flex; align-items: center; gap: 7px; }
  .contact__row svg { width: 13px; height: 13px; flex: none; }
  .contact__web span { color: var(--brand-blue); }

  .wave { position: absolute; left: 0; bottom: 0; width: 620px; height: 354px; }
</style>
</head>
<body>

<section class="card card--front" aria-label="Card front">
  <div class="brand">
    <span class="brand__mark"></span>
    <span class="brand__name">
      <span class="brand__line1">RK Ledgerwise</span>
      <span class="brand__line2">&amp; Filing Partners, LLC</span>
    </span>
  </div>
</section>

<section class="card card--back" aria-label="Card back">
  <svg class="wave" viewBox="0 0 620 354" preserveAspectRatio="none" aria-hidden="true">
    <path d="M0,325 C220,318 420,300 500,225 C545,182 580,150 620,140 L620,354 L0,354 Z" fill="var(--brand-blue)"/>
    <path d="M0,322 C230,314 410,290 490,215 C535,172 575,142 620,132 L620,138 C582,148 548,176 505,218 C425,296 225,316 0,325 Z" fill="var(--slate)"/>
  </svg>

  <div class="brand">
    <span class="brand__mark"></span>
    <span class="brand__name">
      <span class="brand__line1">RK Ledgerwise</span>
      <span class="brand__line2">&amp; Filing Partners, LLC</span>
    </span>
  </div>

  <div class="divider"></div>

  <div class="contact">
    <div class="contact__name">Malcolm Ferris, CPA</div>
    <div class="contact__role">Owner</div>
    <div>4736 Ferncliff Ave #2093</div>
    <div style="margin-bottom:6px">Dunmore Falls, MD 21990</div>
    <div class="contact__row">
      <svg viewBox="0 0 16 16"><path d="M3 2h3l1.5 4-2 1.2a9 9 0 0 0 3.3 3.3L10 8.5l4 1.5v3c0 .6-.4 1-1 1A12 12 0 0 1 2 3c0-.6.4-1 1-1z" fill="var(--brand-blue)"/></svg>
      <span>(240) 555-0148</span>
    </div>
    <div class="contact__row">
      <svg viewBox="0 0 16 16"><rect x="1" y="3" width="14" height="10" fill="var(--brand-blue)"/><path d="M1 3l7 6 7-6" fill="none" stroke="#fff" stroke-width="1.3"/></svg>
      <span>Mferris@rkledgerwise.example</span>
    </div>
    <div class="contact__row contact__web">
      <svg viewBox="0 0 16 16"><circle cx="8" cy="8" r="7" fill="var(--brand-blue)"/><path d="M1 8h14M8 1c-3 3.5-3 10.5 0 14M8 1c3 3.5 3 10.5 0 14" fill="none" stroke="#fff" stroke-width="0.9"/></svg>
      <span>www.<span>Rkledgerwise.example</span></span>
    </div>
  </div>
</section>

</body>
</html>
```